A5 Flyer & A3 poster design for Fizz Lobes

Fizz Lobes are a fun new accesories brand based in the UK

Create an A5 Flyer , A4 poster and simple website under construction landing page.

1. A5 Flyer - Portrait

- Hand drawn example attached showing rough layout. To include 6 pictures (attached) in polaroid format hung on a line using pegs.
- Pictures to be cropped to fit in 6 same size boxes.
- Logo attached
- NEW to be written in the same pink as logo.
- Create a background in keeping with the style of the logo and images

2. A4 poster - Portrait

- The same style , colour and font as the Flyer.
- The same six images just bigger.
- Example layout attached.

COPY FOR FLYER

Brand New Quality Clip-on ears
Soft & light weight for comfortable wear
Perfect for parties, festivals & nights out
Available in a variety of quality faux fur colours with sparkle or velour centre
Great for adults or kids

Email: hello@fizzlobes.co.uk
Call: 07913 284 517
Web: www.fizzlobes.co.uk

Target Market(s)

Females 18 - 40

Industry/Entity Type

Construction

Requirements
Must have
• must be modern. no dated flyer backgrounds

```html
<!DOCTYPE html>
<html lang="en">
<head>
<meta charset="utf-8">
<title>Fizz Lobes – A5 Flyer</title>
<link rel="stylesheet" href="https://fonts.googleapis.com/css2?family=Fredoka:wght@600&family=Questrial&display=swap">
<style>
  :root {
    --pink: #e4127f;
    --pink-deep: #c70c6c;
    --pink-soft: #f27ab8;
    --pink-pale: #fbd3e8;
    --ink: #2b2b2b;
    --paper: #ffffff;
    --backdrop: #ececec;
    --frame-shadow: rgba(0,0,0,0.25);
    --photo-warm: #b48a74;
    --photo-dark: #4a3a36;
  }
  * { box-sizing: border-box; margin: 0; padding: 0; }
  html, body { width: 1200px; height: 1200px; overflow: hidden; background: var(--backdrop); }
  .canvas { position: relative; width: 1200px; height: 1200px; }
  .flyer {
    position: absolute; left: 210px; top: 50px; width: 780px; height: 1100px;
    background: var(--paper); overflow: hidden;
    box-shadow: 0 10px 40px rgba(0,0,0,0.18);
    font-family: "Questrial", sans-serif; color: var(--ink);
  }
  .swoosh, .band-art { position: absolute; left: 0; top: 0; }
  .brand {
    position: absolute; left: 70px; top: 170px;
    font-family: "Fredoka", sans-serif; font-weight: 600;
    font-size: 64px; line-height: 1; color: var(--pink);
    display: flex; align-items: center; gap: 14px;
  }
  .brand-dot { width: 18px; height: 18px; border-radius: 50%; background: var(--pink); }
  .badge-new {
    position: absolute; left: 430px; top: 40px; width: 200px; height: 200px;
    border-radius: 50%; background: #d9d9d9; padding: 12px;
  }
  .badge-new span {
    display: flex; align-items: center; justify-content: center;
    width: 100%; height: 100%; border-radius: 50%;
    background: radial-gradient(circle at 40% 35%, var(--pink-soft), var(--pink) 60%, var(--pink-deep));
    color: var(--paper); font-family: "Fredoka", sans-serif; font-weight: 600; font-size: 62px;
  }
  .product-card {
    position: absolute; width: 210px; height: 122px; background: var(--paper);
    padding: 10px; box-shadow: 2px 4px 10px var(--frame-shadow);
  }
  .product-card .photo { width: 100%; height: 100%; border: 1px solid var(--pink); }
  .product-card--tan { left: 505px; top: 258px; transform: rotate(-6deg); }
  .product-card--tan .photo { background: radial-gradient(ellipse at center, #d9b99a, #f4ece4 75%); }
  .product-card--black { left: 535px; top: 395px; transform: rotate(-3deg); }
  .product-card--black .photo { background: radial-gradient(ellipse at center, #8e1030, #1d1416 55%, #f6f0f2 80%); }
  .pin { position: absolute; top: -8px; left: 50%; width: 12px; height: 12px; margin-left: -6px;
    border-radius: 50%; background: var(--pink); box-shadow: 1px 2px 3px rgba(0,0,0,0.3); }
  .features { position: absolute; left: 55px; top: 340px; width: 420px; list-style: none; }
  .features li {
    position: relative; padding-left: 40px; font-size: 19px; line-height: 1.25; margin-bottom: 12px;
  }
  .features svg { position: absolute; left: 0; top: 2px; width: 26px; height: 22px; }
  .polaroid {
    position: absolute; width: 210px; height: 165px; background: var(--paper);
    padding: 14px 14px 30px; box-shadow: 3px 5px 12px var(--frame-shadow);
  }
  .polaroid .photo { width: 100%; height: 100%; }
  .polaroid--1 { left: 45px;  top: 620px; }
  .polaroid--2 { left: 285px; top: 584px; }
  .polaroid--3 { left: 525px; top: 550px; }
  .polaroid--4 { left: 45px;  top: 803px; }
  .polaroid--5 { left: 285px; top: 767px; }
  .polaroid--6 { left: 525px; top: 733px; }
  .photo--warm { background: linear-gradient(135deg, #d8b9a6, var(--photo-warm) 55%, #e8d9cf); }
  .photo--night { background: linear-gradient(135deg, #3a2e2c, var(--photo-dark) 50%, #a88372); }
  .tagline {
    position: absolute; left: 560px; top: 920px; list-style: none;
    font-family: "Fredoka", sans-serif; font-weight: 600; font-size: 38px; color: var(--pink);
  }
  .tagline li { position: relative; padding-left: 40px; line-height: 1.2; }
  .tagline svg { position: absolute; left: 0; top: 12px; width: 28px; height: 24px; }
  .contact { position: absolute; left: 60px; top: 990px; list-style: none; font-size: 22px; }
  .contact li { display: flex; align-items: center; gap: 14px; line-height: 1.35; }
  .contact svg { width: 16px; height: 16px; fill: var(--pink); flex: none; }
</style>
</head>
<body>
<div class="canvas">
  <article class="flyer">
    <svg class="swoosh" width="780" height="340" viewBox="0 0 780 340" aria-hidden="true">
      <path d="M0 290 C 260 310 560 260 780 70 L 780 0 C 700 180 430 280 0 280 Z" fill="var(--pink)"/>
      <path d="M0 300 C 300 318 600 250 780 100" fill="none" stroke="var(--pink)" stroke-width="3"/>
    </svg>

    <svg class="band-art" width="780" height="1100" viewBox="0 0 780 1100" aria-hidden="true">
      <defs>
        <linearGradient id="bandFill" x1="0" y1="0" x2="1" y2="1">
          <stop offset="0" stop-color="var(--pink-soft)"/>
          <stop offset="0.5" stop-color="var(--pink)"/>
          <stop offset="1" stop-color="var(--pink-deep)"/>
        </linearGradient>
      </defs>
      <path d="M0 660 L 780 540 L 780 850 L 0 960 Z" fill="url(#bandFill)"/>
      <path d="M0 780 C 250 720 500 740 780 640" fill="none" stroke="var(--pink-pale)" stroke-width="2" opacity="0.5"/>
      <path d="M0 840 C 260 780 520 810 780 710" fill="none" stroke="var(--pink-pale)" stroke-width="2" opacity="0.35"/>
      <path d="M520 1100 C 460 1020 470 940 560 885" fill="none" stroke="var(--pink)" stroke-width="10"/>
      <path d="M545 1100 C 490 1030 495 960 575 905" fill="none" stroke="var(--pink)" stroke-width="3"/>
    </svg>

    <div class="brand"><span class="brand-dot"></span>Fizz Lobes</div>

    <div class="badge-new"><span>New</span></div>

    <figure class="product-card product-card--tan"><i class="pin"></i>
      <div class="photo" role="img" aria-label="Product photo: pair of tan faux fur clip-on ears with sparkle centres"></div>
    </figure>
    <figure class="product-card product-card--black"><i class="pin"></i>
      <div class="photo" role="img" aria-label="Product photo: pair of black faux fur clip-on ears with red velour centres"></div>
    </figure>

    <ul class="features">
      <li><svg viewBox="0 0 26 22"><path d="M13 20 C4 13 1 9 3 5 C5 1 10 1 13 5 C16 1 21 1 23 5 C25 9 22 13 13 20Z" fill="none" stroke="var(--pink)" stroke-width="3"/></svg>Brand New Quality Clip-on ears</li>
      <li><svg viewBox="0 0 26 22"><path d="M13 20 C4 13 1 9 3 5 C5 1 10 1 13 5 C16 1 21 1 23 5 C25 9 22 13 13 20Z" fill="none" stroke="var(--pink)" stroke-width="3"/></svg>Soft &amp; light weight for comfortable wear</li>
      <li><svg viewBox="0 0 26 22"><path d="M13 20 C4 13 1 9 3 5 C5 1 10 1 13 5 C16 1 21 1 23 5 C25 9 22 13 13 20Z" fill="none" stroke="var(--pink)" stroke-width="3"/></svg>Perfect for parties, festivals &amp; nights out</li>
      <li><svg viewBox="0 0 26 22"><path d="M13 20 C4 13 1 9 3 5 C5 1 10 1 13 5 C16 1 21 1 23 5 C25 9 22 13 13 20Z" fill="none" stroke="var(--pink)" stroke-width="3"/></svg>Available in a variety of quality faux fur colours with sparkle or velour centre</li>
      <li><svg viewBox="0 0 26 22"><path d="M13 20 C4 13 1 9 3 5 C5 1 10 1 13 5 C16 1 21 1 23 5 C25 9 22 13 13 20Z" fill="none" stroke="var(--pink)" stroke-width="3"/></svg>Great for adults or kids</li>
    </ul>

    <figure class="polaroid polaroid--1"><i class="pin"></i><div class="photo photo--warm" role="img" aria-label="Photo: group of three friends wearing clip-on ears"></div></figure>
    <figure class="polaroid polaroid--2"><i class="pin"></i><div class="photo photo--night" role="img" aria-label="Photo: two friends on a night out wearing clip-on ears"></div></figure>
    <figure class="polaroid polaroid--3"><i class="pin"></i><div class="photo photo--night" role="img" aria-label="Photo: young woman with blonde hair wearing clip-on ears"></div></figure>
    <figure class="polaroid polaroid--4"><i class="pin"></i><div class="photo photo--warm" role="img" aria-label="Photo: smiling woman wearing clip-on ears"></div></figure>
    <figure class="polaroid polaroid--5"><i class="pin"></i><div class="photo photo--warm" role="img" aria-label="Photo: close-up of a woman wearing clip-on ears"></div></figure>
    <figure class="polaroid polaroid--6"><i class="pin"></i><div class="photo photo--warm" role="img" aria-label="Photo: two girls wearing pink clip-on ears"></div></figure>

    <ul class="tagline">
      <li><svg viewBox="0 0 26 22"><path d="M13 20 C4 13 1 9 3 5 C5 1 10 1 13 5 C16 1 21 1 23 5 C25 9 22 13 13 20Z" fill="none" stroke="var(--pink)" stroke-width="3"/></svg>Play Full</li>
      <li><svg viewBox="0 0 26 22"><path d="M13 20 C4 13 1 9 3 5 C5 1 10 1 13 5 C16 1 21 1 23 5 C25 9 22 13 13 20Z" fill="none" stroke="var(--pink)" stroke-width="3"/></svg>Fun</li>
    </ul>

    <ul class="contact">
      <li><svg viewBox="0 0 16 16"><path d="M3 1 L6 1 L7 5 L5 6 C6 8 8 10 10 11 L11 9 L15 10 L15 13 C15 14 14 15 13 15 C6 15 1 10 1 3 C1 2 2 1 3 1Z"/></svg>07913 284 517</li>
      <li><svg viewBox="0 0 16 16"><path d="M1 3 H15 V13 H1 Z M1 3 L8 9 L15 3" fill="none" stroke="var(--pink)" stroke-width="2"/></svg>hello@fizzlobes.co.uk</li>
      <li><svg viewBox="0 0 16 16"><circle cx="8" cy="8" r="6.5" fill="none" stroke="var(--pink)" stroke-width="1.6"/><path d="M1.5 8 H14.5 M8 1.5 C5 5 5 11 8 14.5 M8 1.5 C11 5 11 11 8 14.5" fill="none" stroke="var(--pink)" stroke-width="1.3"/></svg>www.fizzlobes.co.uk</li>
    </ul>
  </article>
</div>
</body>
</html>
```